Real Estate Business Card

On the front side I want to have my info, my brokerage info.
On the back side I want have my complany’s logo, website and Facebook link. I will provide all this once I select a design.

I would like to see Black background and gold text, Dark Blue and gold text and White and blue text designs

Font styles to use
Sans Serif
Script

```html
<!DOCTYPE html>
<html lang="en">
<head>
<meta charset="utf-8">
<title>Stonewell Realty – Business Card</title>
<link href="https://fonts.googleapis.com/css2?family=Lato:wght@400;700;900&display=swap" rel="stylesheet">
<style>
  :root {
    --navy: #050b22;
    --paper: #ffffff;
    --backdrop: #ece7dc;
    --ink: #0b1026;
    --shadow: rgba(40, 30, 10, 0.25);
  }
  * { margin: 0; padding: 0; box-sizing: border-box; }
  html, body { width: 1200px; height: 462px; overflow: hidden; }
  body {
    position: relative;
    background: var(--backdrop);
    font-family: "Lato", Arial, sans-serif;
    color: var(--ink);
  }
  .card {
    position: absolute;
    background: var(--paper);
    box-shadow: 0 3px 8px var(--shadow);
  }
  .card--front { left: 84px; top: 84px; width: 516px; height: 294px; }
  .card--back  { left: 633px; top: 88px; width: 511px; height: 289px; }

  .brand-panel {
    position: absolute; left: 0; top: 0;
    width: 249px; height: 100%;
    background: var(--navy);
    display: flex; align-items: center; justify-content: center;
  }
  .brand-name {
    font-weight: 900;
    text-transform: uppercase;
    text-align: center;
    line-height: 1;
    letter-spacing: 0.5px;
  }
  .brand-panel .brand-name { color: var(--paper); font-size: 30px; }
  .card--back .brand-name {
    position: absolute; left: 0; right: 0; top: 138px;
    color: var(--navy); font-size: 34px;
  }

  .contact {
    position: absolute; left: 357px; top: 84px;
    font-size: 9.5px; line-height: 12px;
  }
  .contact__name { font-size: 12px; font-weight: 700; line-height: 14px; }
  .contact__role { font-size: 6px; letter-spacing: 0.3px; text-transform: uppercase; margin-bottom: 16px; }
  .contact__row { position: relative; margin-bottom: 13px; }
  .contact__icon {
    position: absolute; left: -24px; top: 0;
    width: 16px; height: 16px; fill: var(--ink);
  }

  .links {
    position: absolute; left: 190px; top: 225px;
    font-size: 9.5px; font-weight: 700;
  }
  .links__row { display: flex; align-items: center; gap: 12px; margin-bottom: 11px; }
  .links__icon { width: 19px; height: 19px; }
</style>
</head>
<body>
  <section class="card card--front">
    <div class="brand-panel">
      <div class="brand-name">Stonewell<br>Realty</div>
    </div>
    <div class="contact">
      <div class="contact__name">Nora Fielding</div>
      <div class="contact__role">Broker</div>
      <div class="contact__row">
        <svg class="contact__icon" viewBox="0 0 24 24"><path d="M6.6 10.8a15 15 0 0 0 6.6 6.6l2.2-2.2a1 1 0 0 1 1-.25 11.4 11.4 0 0 0 3.6.6 1 1 0 0 1 1 1V20a1 1 0 0 1-1 1A17 17 0 0 1 3 4a1 1 0 0 1 1-1h3.5a1 1 0 0 1 1 1c0 1.25.2 2.45.6 3.6a1 1 0 0 1-.25 1z"/></svg>
        +43215550142<br>+41235550187
      </div>
      <div class="contact__row">
        <svg class="contact__icon" viewBox="0 0 24 24" fill="none" stroke="#0b1026" stroke-width="1.6" style="fill:none"><rect x="2.5" y="5" width="19" height="14"/><path d="M2.5 5l9.5 8 9.5-8"/></svg>
        nora@fieldingbroker.com
      </div>
      <div class="contact__row">
        <svg class="contact__icon" viewBox="0 0 24 24"><path d="M12 2a7 7 0 0 0-7 7c0 5.2 7 13 7 13s7-7.8 7-13a7 7 0 0 0-7-7zm0 9.5A2.5 2.5 0 1 1 12 6.5a2.5 2.5 0 0 1 0 5z"/></svg>
        Harbor Lane 8,<br>CITY<br>1234 CA
      </div>
    </div>
  </section>

  <section class="card card--back">
    <div class="brand-name">Stonewell Realty</div>
    <div class="links">
      <div class="links__row">
        <svg class="links__icon" viewBox="0 0 24 24" fill="none" stroke="#0b1026" stroke-width="1.8"><circle cx="12" cy="12" r="10"/><ellipse cx="12" cy="12" rx="4.5" ry="10"/><path d="M2 12h20M4 7h16M4 17h16"/></svg>
        <span>www.stonewellrealty.com</span>
      </div>
      <div class="links__row">
        <svg class="links__icon" viewBox="0 0 24 24"><circle cx="12" cy="12" r="10" fill="#0b1026"/></svg>
        <span>www.linkpage.com/stonewell</span>
      </div>
    </div>
  </section>
</body>
</html>
```